TalkWell Needs a Business Card

We need a business card for Tomas Kellerby, Ph.D., CCC-SLP, who is affiliated with Lakemont Ridge University. He is an Associate Professor and Licensed Speech-Language Pathologist, Department of Communication Disorders, College of Health and Human Services.

He has a consulting business "TalkWell Consultant". The logo is attached. The consulting company color is Turquoise. LRU school color is orange.

The consulting business focus on: Consultation, Research & Professional Development. Our target market is individuals with annual family income of $100,000.00 or more for consultation and speech-language pathologists for professional development activities.

No harsh colors, subtle colors appreciated. Address, e-mail, telephone, and small scan logo for a link to our website. Creativity in design will be appreciated. Please add your comments, why you created this design?

Thanks and looking for submissions.

```html
<!DOCTYPE html>
<html lang="en">
<head>
<meta charset="utf-8">
<title>TalkWell Consultants – Business Card</title>
<link rel="stylesheet" href="https://fonts.googleapis.com/css2?family=Open+Sans:wght@400;600;700&display=swap">
<style>
  :root {
    --backdrop: #e9e6e2;
    --charcoal: #2a2c2e;
    --charcoal-soft: #3a3d40;
    --turquoise: #6ccfd3;
    --green: #5cc266;
    --paper: #fbfbfa;
    --ink: #2b2d2f;
    --shadow: rgba(0, 0, 0, 0.28);
  }
  * { box-sizing: border-box; margin: 0; padding: 0; }
  html, body {
    width: 1200px;
    height: 800px;
    overflow: hidden;
  }
  body {
    background: var(--backdrop);
    font-family: "Open Sans", Arial, sans-serif;
    position: relative;
  }

  /* Front of card */
  .card-front {
    position: absolute;
    left: 130px;
    top: 110px;
    width: 350px;
    height: 580px;
    background: var(--charcoal);
    box-shadow: 0 10px 30px var(--shadow);
    overflow: hidden;
  }
  .card-front .band-top {
    position: absolute;
    left: 0; right: 0; top: 40px;
    height: 150px;
    background: var(--turquoise);
  }
  .card-front .band-bottom {
    position: absolute;
    left: 0; right: 0; bottom: 40px;
    height: 150px;
    background: var(--green);
  }
  .card-front .wordmark {
    position: absolute;
    left: 50%; top: 50%;
    transform: translate(-50%, -50%) rotate(90deg);
    display: flex;
    align-items: center;
    gap: 14px;
    white-space: nowrap;
  }
  .card-front .wordmark-dot {
    width: 18px; height: 18px;
    border-radius: 50%;
    background: var(--turquoise);
  }
  .card-front .wordmark-name {
    color: #ffffff;
    font-size: 40px;
    font-weight: 400;
    letter-spacing: 0.5px;
  }

  /* Back of card */
  .card-back {
    position: absolute;
    left: 540px;
    top: 220px;
    width: 600px;
    height: 360px;
    background: var(--paper);
    box-shadow: 0 10px 30px var(--shadow);
    overflow: hidden;
  }
  .card-back .brand-strip {
    height: 92px;
    background: var(--charcoal);
    display: flex;
    align-items: center;
    justify-content: flex-end;
    gap: 12px;
    padding: 0 34px;
  }
  .card-back .brand-dot {
    width: 14px; height: 14px;
    border-radius: 50%;
    background: var(--turquoise);
  }
  .card-back .brand-name {
    color: var(--turquoise);
    font-size: 26px;
    font-weight: 400;
  }
  .card-back .accent-line {
    height: 4px;
    background: var(--turquoise);
  }
  .card-back .details {
    position: absolute;
    right: 40px;
    top: 122px;
    text-align: right;
    color: var(--ink);
  }
  .card-back .person-name {
    color: var(--green);
    font-size: 22px;
    font-weight: 700;
    margin-bottom: 8px;
  }
  .card-back .role {
    font-size: 15px;
    line-height: 1.35;
  }
  .card-back .contact {
    position: absolute;
    left: 28px;
    right: 28px;
    bottom: 50px;
    font-size: 14px;
    color: var(--ink);
    display: flex;
    justify-content: space-between;
  }
  .card-back .address-band {
    position: absolute;
    left: 0; right: 0; bottom: 0;
    height: 38px;
    background: var(--turquoise);
    display: flex;
    align-items: center;
    padding: 0 28px;
    font-size: 14px;
    color: var(--charcoal);
    letter-spacing: 0.3px;
  }
</style>
</head>
<body>

  <section class="card-front" aria-label="Card front">
    <div class="band-top"></div>
    <div class="band-bottom"></div>
    <div class="wordmark">
      <span class="wordmark-dot"></span>
      <span class="wordmark-name">TalkWell Consultants</span>
    </div>
  </section>

  <section class="card-back" aria-label="Card back">
    <header class="brand-strip">
      <span class="brand-dot"></span>
      <span class="brand-name">TalkWell Consultants</span>
    </header>
    <div class="accent-line"></div>

    <div class="details">
      <h1 class="person-name">Tomas Kellerby, Ph.D., CCC-SLP</h1>
      <p class="role">Associate Professor</p>
      <p class="role">Licensed Speech-Language Pathologist</p>
      <p class="role">Department of Communication Disorders</p>
      <p class="role">College of Health and Human Services</p>
    </div>

    <div class="contact">
      <span>(555) 310-4472 | tkellerby@talkwellconsultants.com</span>
      <span>talkwellconsultants.com</span>
    </div>

    <footer class="address-band">2140 HARBOR LANE, FAIRVIEW, ANY CITY</footer>
  </section>

</body>
</html>
```